Below Par Parenting

I would like a poster (size to be agreed) created for the wording that I have composed and which I have pasted below. The poster is for my own personal gratification. It is not for commercial use. The message is driven by honesty and a profound sense of mea culpa. I am open to ideas regarding style and presentation.
I am an awful parent. No question. I am not cut out for this shit. I’m too quick to temper. I turn everything into a test of wills. I’m not down for food on the floor, for having my car trashed with your stink and detritus, for having the walls of my house daubed in your greasy fingerprints. I want to listen to The Marrows not Bumble Over Dewfields on repeat. I enjoyed making you but, on reflection, I should have pulled out. Let me go back in time to that great waste of space and energy that is ante-natal classes and tell that boho with the flowery dress and curly hair, ‘Why are you concentrating on the first five seconds? All the pain comes later. Why aren’t you telling us what to do when they won’t sleep, when they won’t sit in their high chairs, when they won’t sleep on the aeroplane?’ Boy, I wish I could play it loosey-goosey like those left-leaning parents I see going ‘coo-coo’ in Brindisetti’s but I’m not built like that. I am a right-wing despot. It’s Nazi Germany back at my place. I’m not interested in your meltdowns and tantrums. You want to writhe on the floor in the car park going red in the face? Make my day. You want to go spastic because I won’t let you watch TV for five hours straight? I don’t give a shit. Read my lips. I won’t pander to it. My wife says you’re babies but all I see is little people with an agenda. I’ve got naughty steps and sin-bins all over the joint. I wish I wasn’t the tyrant, the Valdrumo and the Oko Temba I am but it is what it is. I blame my parents and they, in turn, will blame me and their parents. Understand I don’t want to infect you too much with my bad behavior but if you could stop making such a scene in public places with your screaming, your bitching and your all round refusal to play nice then maybe, just maybe, we’d have a chance and I wouldn’t be such an awful parent.

```html
<!DOCTYPE html>
<html lang="en">
<head>
<meta charset="utf-8">
<title>Below Par Parenting</title>
<link rel="stylesheet" href="https://fonts.googleapis.com/css2?family=Sorts+Mill+Goudy&family=Vollkorn:wght@700&family=Open+Sans:wght@700&display=swap">
<style>
  :root {
    --paper: #ffffff;
    --ink: #2a2622;
    --blue: #3b6fb0;
    --green: #5f8f2e;
    --navy: #23457e;
    --meadow-light: #eef6e2;
    --meadow: #bfdc97;
  }
  html, body { margin: 0; padding: 0; overflow: hidden; }
  body { width: 859px; height: 1200px; background: var(--paper); }
  .poster {
    position: relative; width: 859px; height: 1200px; overflow: hidden;
    background: var(--paper); color: var(--ink);
    font-family: "Sorts Mill Goudy", Georgia, serif;
  }
  .confession {
    position: absolute; left: 82px; top: 58px; width: 712px;
    font-size: 15.4px; line-height: 23.2px;
  }
  .confession p { margin: 0; }
  .headline { font-family: "Vollkorn", Georgia, serif; font-weight: 700; font-size: 30px; line-height: 40px; margin-bottom: 2px; }
  .headline .aside { font-family: "Sorts Mill Goudy", Georgia, serif; font-weight: 400; font-size: 16px; }
  .indent { text-indent: 24px; }
  .tone-blue { color: var(--blue); }
  .tone-green { color: var(--green); }
  .shout { font-family: "Open Sans", Arial, sans-serif; font-weight: 700; font-size: 13px; letter-spacing: -0.2px; }
  .shout.tone-blue { color: var(--navy); }
  .gap { margin-top: 20px !important; }
  .closing {
    position: absolute; left: 170px; top: 690px; width: 370px;
    font-size: 17px; line-height: 27px; margin: 0; text-indent: 24px;
  }
  .meadow {
    position: absolute; left: 0; right: 0; top: 930px; height: 170px;
    background: linear-gradient(to bottom, var(--paper), var(--meadow-light) 40%, var(--paper));
  }
  .illustration {
    position: absolute; left: 558px; top: 700px; width: 245px; height: 320px;
    border-radius: 40px 40px 12px 12px;
    background: radial-gradient(ellipse at 50% 85%, var(--meadow) 0%, var(--meadow-light) 55%, var(--paper) 80%);
  }
</style>
</head>
<body>
<main class="poster">
  <section class="confession">
    <p class="headline">I am an awful parent. <span class="aside">No question.</span></p>
    <p>I am not cut out for this shit. I’m too quick to temper.</p>
    <p>I turn everything into a test of wills.</p>
    <p>I’m not down for food on the floor, for having my car trashed with your stink and detritus, for having the walls of my house daubed in your greasy fingerprints.</p>
    <p class="tone-blue">I want to listen to The Marrows not Bumble Over Dewfields on repeat.</p>
    <p>I enjoyed making you but, on reflection, I should have pulled out.</p>
    <p class="indent">Let me go back in time to that great waste of space and energy that is ante-natal classes and tell that boho with the flowery dress and curly hair, ‘Why are you concentrating on the first five seconds?</p>
    <p class="indent">All the pain comes later.</p>
    <p class="tone-green">Why aren’t you telling us what to do when they won’t sleep, when they won’t sit in their high chairs, when they won’t sleep on the aeroplane?’</p>
    <p class="indent">Boy, I wish I could play it loosey-goosey like those left-leaning parents I see going ‘coo-coo’ in Brindisetti’s but I’m not built like that.</p>
    <p>I am a right-wing despot. It’s Nazi Germany back at my place.</p>
    <p>I’m not interested in your meltdowns and tantrums.</p>
    <p class="tone-green gap">You want to writhe on the floor in the car park going red in the face?</p>
    <p>Make my day.</p>
    <p class="shout tone-blue">You want to go spastic because I won’t let you watch TV for five hours straight?</p>
    <p>I don’t give a shit. Read my lips. I won’t pander to it.</p>
    <p class="shout tone-green">My wife says you’re babies but all I see is little people with an agenda.</p>
    <p class="shout tone-green">I’ve got naughty steps and sin-bins all over the joint.</p>
    <p>I wish I wasn’t the tyrant, the Valdrumo and the Oko Temba I am but it is what it is.</p>
    <p class="shout tone-blue">I blame my parents and they, in turn, will blame me and their parents.</p>
  </section>

  <p class="closing">Understand I don’t want to infect you too much with my bad behavior but if you could stop making such a scene in public places with your screaming, your bitching and your all round refusal to play nice then maybe, just maybe, we’d have a chance and I wouldn’t be such an awful parent.</p>

  <div class="meadow"></div>
  <div class="illustration" role="img" aria-label="Cartoon of a small child in a white shirt and blue trousers running happily across green grass"></div>
</main>
</body>
</html>
```